Organic skincare label - minimalist, earthy, luxe design needed!

I need a label design for a luxury natural skin care line called "Velka Botanix". Velka means 'earth' in Swahili. I would like the design to embody an earthy feel but be minimalistic and give a luxe vibe. My first product will be a Tumeric and Neem Scrub.

The size of the jar is 8oz, label dimensions should be (1.625" Tall x 8.5" Wide)
I will be making other products too such as; oils + toners so I feel free to do labels for glass bottles and/or spray bottles as well.

Forest green, light pinks/nudes/beige, grey, white, gold, are colors that can be used (not all have to be used).

I have included pictures of some things I've worked on myself as well as my original logo design but I need to simplify the logo, no circle around it.
Feel free to get creative.

Thank you! :)
Updates

Target Market(s)

Socially Conscious, Beauty Enthusiast, Minimalist

Industry/Entity Type

Skin Care

Font styles to use
Sans Serif
Other font styles liked:
• "Wonderlove doodle" is the font used for "Velka" in the logo. Feel free to use that or change it as you see fit.

Requirements
Must have
• Simplistic design
would like to stick to a font close to the ones in the logo. Either the one used for the name "Velka" OR the one that the slogan "soil & soul" uses.

I have also included some pictures to capture the aesthetic of my social media and website.

Gender neutral

```html
<!DOCTYPE html>
<html lang="en">
<head>
<meta charset="utf-8">
<title>Velka Botanix – Tumeric and Neem Scrub labels</title>
<link href="https://fonts.googleapis.com/css2?family=Open+Sans:wght@400;600;700&family=Overlock:wght@400&display=swap" rel="stylesheet">
<style>
  :root {
    --bg: #faf3e2;
    --white: #ffffff;
    --tan: #d4b595;
    --cream: #f8f1de;
    --sand: #e8dcb2;
    --pale-claim: #e6d6a6;
    --art: #eadcae;
    --brown: #a57350;
    --brown-dark: #8b5a3c;
    --ink-ingredient: #9a7457;
    --cream-text: #f7eedb;
    --muted-brand: #d9bf9e;
    --forest: #1d4a2b;
  }
  * { box-sizing: border-box; margin: 0; padding: 0; }
  html, body {
    width: 1167px; height: 1200px; overflow: hidden;
    background: var(--bg);
    font-family: "Open Sans", Arial, sans-serif;
  }
  .board { position: relative; width: 1167px; height: 1200px; }
  .label {
    position: absolute; left: 88px; width: 991px; height: 189px;
    background: var(--white); overflow: hidden;
    box-shadow: 0 2px 8px rgba(120, 95, 60, 0.18);
  }
  .label--tan { top: 170px; }
  .label--cream { top: 505px; }
  .label--white { top: 840px; }
  .bands { position: absolute; inset: 0; width: 991px; height: 189px; }
  .globe-art {
    position: absolute; left: 18px; top: 12px; width: 110px; height: 140px;
    background: radial-gradient(ellipse at 50% 45%, var(--art) 0%, rgba(234, 220, 174, 0.35) 70%, rgba(234, 220, 174, 0) 100%);
  }
  .claims {
    position: absolute; left: 147px; top: 22px;
    list-style: none; color: var(--pale-claim);
    font-size: 10px; line-height: 13px;
  }
  .maker {
    position: absolute; left: 147px; top: 150px;
    font-size: 8px; line-height: 9.5px; color: var(--brown-dark);
  }
  .maker strong { font-weight: 700; }
  .maker-mark {
    position: absolute; left: 93px; top: 160px;
    font-weight: 700; font-size: 13px; color: var(--brown-dark);
  }
  .brand-center {
    position: absolute; left: 369px; width: 300px; top: 70px; text-align: center;
  }
  .brand-center .name { font-weight: 700; font-size: 40px; line-height: 44px; letter-spacing: 1px; }
  .brand-center .tagline { font-size: 12px; line-height: 16px; margin-top: 2px; letter-spacing: 0.3px; }
  .product-name {
    position: absolute; left: 369px; width: 300px; top: 142px; text-align: center;
    font-family: "Overlock", "Open Sans", sans-serif; font-size: 24px; letter-spacing: 0.6px;
  }
  .brand-side { position: absolute; left: 664px; width: 180px; top: 40px; text-align: center; }
  .brand-side .name { font-weight: 700; font-size: 30px; line-height: 34px; color: var(--brown); }
  .brand-side .tagline { font-size: 9.5px; line-height: 12px; color: var(--brown-dark); margin-top: 1px; }
  .ingredients {
    position: absolute; left: 704px; top: 103px; width: 235px;
    font-size: 8px; line-height: 9.7px; color: var(--ink-ingredient);
  }
  .ingredients h3 { font-size: 8.5px; font-weight: 700; color: var(--brown-dark); }

  .label--tan .brand-center { color: var(--cream-text); }
  .label--tan .product-name { color: var(--cream-text); }
  .label--cream .brand-center { color: var(--muted-brand); }
  .label--cream .product-name { color: var(--brown-dark); }
  .label--white .brand-center { color: var(--brown); }
  .label--white .product-name { color: var(--forest); }
</style>
</head>
<body>
<main class="board">

  <section class="label label--tan" aria-label="Scrub label, tan version">
    <svg class="bands" viewBox="0 0 991 189" aria-hidden="true">
      <polygon points="271,0 297,0 368,189 341,189" fill="var(--cream)"/>
      <polygon points="297,0 893,0 963,189 368,189" fill="var(--tan)"/>
      <polygon points="893,0 917,0 991,189 963,189" fill="var(--cream)"/>
    </svg>
    <div class="globe-art" role="img" aria-label="Illustration of a child blowing a globe made of leaves and bubbles"></div>
    <ul class="claims">
      <li>Hypoallergenic</li><li>Dermatologist tested</li><li>Cruelty FREE</li><li>Parabens FREE</li>
      <li>Sulfates FREE</li><li>Phthalates FREE</li><li>Alcohol FREE</li><li>Vegan</li>
    </ul>
    <span class="maker-mark">Velka</span>
    <p class="maker">Crafted by:<br><strong>Velka Botanix</strong><br>bla-bla-bla 12345 bla bla bla</p>
    <div class="brand-center"><p class="name">Velka</p><p class="tagline">soil &amp; soul</p></div>
    <p class="product-name">Tumeric and Neem Scrub</p>
    <div class="brand-side"><p class="name">Velka</p><p class="tagline">soil &amp; soul</p></div>
    <div class="ingredients">
      <h3>Ingredients</h3>
      <p>Just a sample of ingredients, Panthenol, Polyglyceryl-10 Laurate, Polyglyceryl-10 Myristate, Glycerine, Arginine, Allantoin, Asiaticoside, Asiatic acid, Madecassic acid, Sodium Hyaluronate, Gardenia Florida Fruit Extract, Citrus Aurantium Bergamia (Bergamot) Fruit Oil, Menthyl Lactate, Mentha Haplocalix Extract</p>
    </div>
  </section>

  <section class="label label--cream" aria-label="Scrub label, cream version">
    <svg class="bands" viewBox="0 0 991 189" aria-hidden="true">
      <polygon points="271,0 297,0 368,189 341,189" fill="var(--sand)"/>
      <polygon points="297,0 893,0 963,189 368,189" fill="var(--cream)"/>
      <polygon points="893,0 917,0 991,189 963,189" fill="var(--sand)"/>
    </svg>
    <div class="globe-art" role="img" aria-label="Illustration of a child blowing a globe made of leaves and bubbles"></div>
    <ul class="claims">
      <li>Hypoallergenic</li><li>Dermatologist tested</li><li>Cruelty FREE</li><li>Parabens FREE</li>
      <li>Sulfates FREE</li><li>Phthalates FREE</li><li>Alcohol FREE</li><li>Vegan</li>
    </ul>
    <span class="maker-mark">Velka</span>
    <p class="maker">Crafted by:<br><strong>Velka Botanix</strong><br>bla-bla-bla 12345 bla bla bla</p>
    <div class="brand-center"><p class="name">Velka</p><p class="tagline">soil &amp; soul</p></div>
    <p class="product-name">Tumeric and Neem Scrub</p>
    <div class="brand-side"><p class="name">Velka</p><p class="tagline">soil &amp; soul</p></div>
    <div class="ingredients">
      <h3>Ingredients</h3>
      <p>Just a sample of ingredients, Panthenol, Polyglyceryl-10 Laurate, Polyglyceryl-10 Myristate, Glycerine, Arginine, Allantoin, Asiaticoside, Asiatic acid, Madecassic acid, Sodium Hyaluronate, Gardenia Florida Fruit Extract, Citrus Aurantium Bergamia (Bergamot) Fruit Oil, Menthyl Lactate, Mentha Haplocalix Extract</p>
    </div>
  </section>

  <section class="label label--white" aria-label="Scrub label, white version">
    <div class="globe-art" role="img" aria-label="Illustration of a child blowing a globe made of leaves and bubbles"></div>
    <ul class="claims">
      <li>Hypoallergenic</li><li>Dermatologist tested</li><li>Cruelty FREE</li><li>Parabens FREE</li>
      <li>Sulfates FREE</li><li>Phthalates FREE</li><li>Alcohol FREE</li><li>Vegan</li>
    </ul>
    <span class="maker-mark">Velka</span>
    <p class="maker">Crafted by:<br><strong>Velka Botanix</strong><br>bla-bla-bla 12345 bla bla bla</p>
    <div class="brand-center"><p class="name">Velka</p><p class="tagline">soil &amp; soul</p></div>
    <p class="product-name">Tumeric and Neem Scrub</p>
    <div class="brand-side"><p class="name">Velka</p><p class="tagline">soil &amp; soul</p></div>
    <div class="ingredients">
      <h3>Ingredients</h3>
      <p>Just a sample of ingredients, Panthenol, Polyglyceryl-10 Laurate, Polyglyceryl-10 Myristate, Glycerine, Arginine, Allantoin, Asiaticoside, Asiatic acid, Madecassic acid, Sodium Hyaluronate, Gardenia Florida Fruit Extract, Citrus Aurantium Bergamia (Bergamot) Fruit Oil, Menthyl Lactate, Mentha Haplocalix Extract</p>
    </div>
  </section>

</main>
</body>
</html>
```